Australia Banner

Use same measuremenbts used for portugal, but ad to say something about 120,000+ New listings now available in Australia
Updates

the 2 banners should be the following sizes 448x81px 197x650px using gif format saying to click here for over 120000 new Australian Listings

look at the website www.tallowhomestead.com and check the portugal banner on the right, the australia banner will be on the left, and within the site on the top area mentioning agent offer. Use a graphic and GIF preferred.

```html
<!DOCTYPE html>
<html lang="en">
<head>
<meta charset="utf-8">
<title>Tallow Homestead – Australia Listings</title>
<link href="https://fonts.googleapis.com/css2?family=Open+Sans:wght@400;600;700&family=Oswald:wght@400;500;600&display=swap" rel="stylesheet">
<style>
:root{
  --green:#6a9a2f;
  --green-dark:#5a8a2a;
  --green-btn:#5f9a47;
  --nav-top:#86b241;
  --nav-bottom:#5f8f2b;
  --slate:#3e4a54;
  --red:#e3232b;
  --promo-green:#78bb5e;
  --beige:#ebe5d1;
  --panel-border:#cfcfcf;
  --text:#3a3a3a;
  --muted:#8a8a8a;
  --grey-bar:#e6e6e6;
  --side-bg:#e4e4e4;
  --tag-bg:#ede7d6;
}
*{box-sizing:border-box;margin:0;padding:0}
html,body{width:1200px;height:927px;overflow:hidden}
body{position:relative;background:var(--beige);font-family:"Open Sans",Arial,sans-serif;color:var(--text)}
.abs{position:absolute}

/* header */
.site-header{left:0;top:0;width:1200px;height:153px;background:#fff}
.brand{left:18px;top:52px;font-size:46px;font-weight:600;color:var(--green);letter-spacing:-1px;line-height:1}
.promo{left:551px;top:36px;width:442px;height:80px;background:var(--promo-green);display:flex;font-family:"Oswald",sans-serif;text-transform:uppercase}
.promo-tag{width:140px;background:var(--red);color:#fff;font-size:29px;font-weight:500;line-height:30px;letter-spacing:2px;padding:9px 0 0 14px;clip-path:polygon(0 0,100% 0,88% 100%,0 100%)}
.promo-body{flex:1;color:#fff;text-align:center;font-size:19px;line-height:23px;padding-top:5px}
.promo-body .cta{display:block;color:#1e2a12;font-size:14px;margin-top:3px}
.promo-arrow{left:970px;top:92px}
.langs{left:551px;top:123px;display:flex;gap:10px;font-size:12px;color:var(--green-dark)}
.langs span{display:flex;align-items:center;gap:5px}
.flag{width:14px;height:9px;display:inline-block}

/* nav */
.main-nav{left:0;top:153px;width:1200px;height:100px;background:linear-gradient(var(--nav-top),var(--nav-bottom))}
.nav-strip{left:0;top:253px;width:1200px;height:6px;background:var(--slate)}
.nav-link{top:171px;color:#fff;font-size:14px;font-weight:700}

/* search */
.search-panel{left:18px;top:202px;width:964px;height:170px;background:#fff;border:1px solid var(--panel-border);border-radius:8px}
.search-input{left:50px;top:228px;width:780px;height:54px;border:1px solid #ccc;border-radius:6px;display:flex;align-items:center;padding-left:15px;gap:12px;color:#c4c4c4;font-size:19px;font-weight:600}
.search-btn{left:858px;top:232px;width:91px;height:46px;background:var(--green-btn);border-radius:5px;color:#fff;font-size:18px;font-weight:700;display:flex;align-items:center;justify-content:center;box-shadow:0 2px 0 #3d6b2b}
.field-label{top:298px;font-size:13px;font-weight:700;color:#333}
.select{top:320px;height:30px;border:1px solid #ccc;border-radius:4px;font-size:12px;color:#555;padding:8px 0 0 9px}
.select::after{content:"";position:absolute;right:0;top:0;width:18px;height:28px;border-left:1px solid #ccc}
.select i{position:absolute;right:5px;top:8px;font-style:normal;font-size:7px;line-height:6px;color:#888}

/* hero */
.hero-copy{left:40px;top:395px;font-size:28px;line-height:36px;color:#3b4a55}
.hero-copy b{font-weight:700}
.hero-btn{left:40px;top:527px;width:219px;height:44px;background:var(--green-btn);border-radius:4px;color:#fff;font-size:18px;font-weight:700;display:flex;align-items:center;justify-content:center;box-shadow:0 2px 2px rgba(0,0,0,.25)}
.photo{border:6px solid #fff;box-shadow:0 2px 6px rgba(0,0,0,.3)}

/* listings */
.content{left:6px;top:605px;width:989px;height:322px;background:#fff}
.tab-bar{left:6px;top:605px;width:989px;height:57px;background:var(--grey-bar)}
.tab{left:246px;top:605px;width:178px;height:57px;background:#dcdcdc;color:#666;font-size:14px;font-weight:700;display:flex;align-items:center;justify-content:center}
.sidebar-left{left:6px;top:662px;width:240px;height:265px;border-right:1px solid #e2e2e2}
.side-title{left:28px;top:691px;font-size:16px;font-weight:700;color:var(--green-dark);line-height:19px}
.video{left:28px;top:740px;width:196px;height:110px;border:1px solid #ccc;background:linear-gradient(135deg,#f3e6c8,#d8c9a6)}
.rule{left:28px;top:869px;width:192px;height:1px;background:#e0e0e0}
.newsletter{left:28px;top:895px;font-size:16px;font-weight:700;color:var(--green-dark);display:flex;align-items:center;gap:10px}
.sort-label{left:260px;top:700px;font-size:12px;color:#444}
.listing-photo{left:246px;top:759px;width:350px;height:168px;background:linear-gradient(#3f8ee0 0%,#7db6ef 45%,#a0765a 70%,#6d5a48 100%)}
.listing-title{left:611px;top:759px;font-size:15px;font-weight:700;color:var(--green-dark)}
.meta-row{left:596px;top:788px;width:397px;height:37px;background:var(--tag-bg);display:flex;font-size:14px}
.meta-row div{display:flex;align-items:center;padding:0 14px}
.meta-row .deal{background:var(--slate);color:#fff;padding:0 16px}
.feat-row{left:596px;top:826px;width:397px;height:38px;background:#f4f4f4;display:flex;font-size:14px}
.feat-row div{display:flex;align-items:center;gap:14px;padding:0 14px;border-right:1px solid #ddd}
.feat-row .loc{border:0;font-size:12px;line-height:14px;gap:10px;font-weight:600;color:#444}
.size{left:611px;top:875px;font-size:11px;color:#333}
.size b{font-size:14px;font-weight:400}
.desc{left:611px;top:917px;font-size:14px;font-weight:600;color:#333}
.agent-badge{left:826px;top:902px;width:168px;height:25px;background:#a59f1c}

/* australia banner */
.au-banner{left:1004px;top:268px;width:196px;height:642px;background:var(--side-bg);border:1px solid #cfcfcf;text-align:center;font-family:"Oswald",sans-serif}
.au-count{position:absolute;left:0;width:100%;top:8px;font-size:56px;font-weight:600;color:var(--green);line-height:1}
.au-plus{position:absolute;left:68px;top:72px}
.au-line{position:absolute;left:0;width:100%;font-size:33px;line-height:34px;color:#333;font-weight:400}
.au-country{position:absolute;left:0;width:100%;top:237px;font-size:38px;font-weight:600;color:var(--green)}
.au-art{position:absolute;left:8px;top:290px;width:178px;height:300px;background:linear-gradient(#e9e9e9 0%,#2a3f9a 20%,#2a3f9a 45%,#d8d8d8 55%,#e94b3c 70%,#d0a080 100%)}
.au-cta{position:absolute;left:18px;top:598px;width:158px;height:36px;border:2px solid #fff;border-radius:18px;background:var(--green-btn);color:#fff;font-size:21px;line-height:32px;font-weight:500}
</style>
</head>
<body>

<header class="abs site-header">
  <div class="abs brand">tallowhomestead.com</div>
</header>

<a class="abs promo">
  <div class="promo-tag">Special<br>Offer</div>
  <div class="promo-body">To subscribe for<br>agents, brokers &amp; developers<span class="cta">Click here</span></div>
</a>
<svg class="abs promo-arrow" width="22" height="22" viewBox="0 0 22 22"><path d="M3 3 L19 11 L12 12 L18 19 L15 21 L9 14 L4 18 Z" fill="var(--green-dark)" stroke="#fff" stroke-width="1.5"/></svg>

<div class="abs langs">
  <span><i class="flag" style="background:#de2910"></i>Chinese</span>
  <span><i class="flag" style="background:#fff;box-shadow:inset 0 0 0 3px #fff,inset 0 0 0 8px #bc002d"></i>Japanese</span>
  <span><i class="flag" style="background:repeating-linear-gradient(#0d5eaf 0 2px,#fff 2px 4px)"></i>Greek</span>
  <span><i class="flag" style="background:linear-gradient(#000 33%,#d00 33% 66%,#ffce00 66%)"></i>German</span>
  <span><i class="flag" style="background:linear-gradient(90deg,#009246 33%,#fff 33% 66%,#ce2b37 66%)"></i>Italian</span>
  <span><i class="flag" style="background:linear-gradient(90deg,#0055a4 33%,#fff 33% 66%,#ef4135 66%)"></i>French</span>
</div>

<nav class="abs main-nav"></nav>
<div class="abs nav-strip"></div>
<a class="abs nav-link" style="left:39px">Home</a>
<a class="abs nav-link" style="left:125px">Buy</a>
<a class="abs nav-link" style="left:196px">Rent</a>
<a class="abs nav-link" style="left:275px">List Your Property</a>
<a class="abs nav-link" style="left:446px">Blog</a>
<a class="abs nav-link" style="left:520px">Contact</a>
<a class="abs nav-link" style="left:814px">Sign in</a>
<a class="abs nav-link" style="left:889px">Register</a>

<section class="abs search-panel"></section>
<div class="abs search-input">
  <svg width="32" height="28" viewBox="0 0 32 28"><circle cx="11" cy="11" r="8" fill="none" stroke="#d0d0d0" stroke-width="3"/><path d="M17 17 L28 26" stroke="#d0d0d0" stroke-width="5" stroke-linecap="round"/></svg>
  Type in your country or city (eg. Rome, Sydney, Greece)
</div>
<div class="abs search-btn">Search</div>

<div class="abs field-label" style="left:50px">Select Country</div>
<div class="abs field-label" style="left:260px">Property Type</div>
<div class="abs field-label" style="left:397px">Bedrooms</div>
<div class="abs field-label" style="left:533px">Bathrooms</div>
<div class="abs field-label" style="left:670px">Price range:</div>
<div class="abs select" style="left:50px;width:185px">Any<i>▲<br>▼</i></div>
<div class="abs select" style="left:260px;width:111px">Any<i>▲<br>▼</i></div>
<div class="abs select" style="left:397px;width:111px">Any<i>▲<br>▼</i></div>
<div class="abs select" style="left:533px;width:111px">Any<i>▲<br>▼</i></div>
<div class="abs select" style="left:670px;width:185px">Any<i>▲<br>▼</i></div>

<div class="abs hero-copy">List your property on the largest<br>online global property marketplace<br>for <b>only $99</b>.</div>
<div class="abs hero-btn">Free Registration</div>

<div class="abs photo" role="img" aria-label="Harbour bridge seen from a waterside living room" style="left:345px;top:478px;width:215px;height:150px;transform:rotate(-4deg);background:linear-gradient(#c9d8e6,#8fa9bd 55%,#6b6256)"></div>
<div class="abs photo" role="img" aria-label="New York skyline with the Empire State Building" style="left:530px;top:382px;width:320px;height:250px;transform:rotate(-4deg);background:linear-gradient(#cdd8e3,#8f9aa6 50%,#5e5f62)"></div>
<div class="abs photo" role="img" aria-label="Eiffel Tower framed by Paris apartment buildings" style="left:738px;top:392px;width:280px;height:240px;transform:rotate(-6deg);background:linear-gradient(90deg,#e6dccb,#a7b9cf 45%,#c9b394)"></div>

<section class="abs content"></section>
<div class="abs tab-bar"></div>
<div class="abs tab">Featured Properties</div>
<aside class="abs sidebar-left"></aside>
<div class="abs side-title">Watch How Tallow<br>Homestead Works</div>
<div class="abs video" role="img" aria-label="Explainer video thumbnail with a play button"></div>
<svg class="abs" style="left:96px;top:765px" width="60" height="60" viewBox="0 0 60 60"><circle cx="30" cy="30" r="29" fill="#fff" opacity=".85"/><path d="M23 17 L44 30 L23 43 Z" fill="#7ab24a"/></svg>
<div class="abs rule"></div>
<div class="abs newsletter">Newsletter
  <svg width="22" height="15" viewBox="0 0 22 15"><rect width="22" height="15" rx="1" fill="var(--green-dark)"/><path d="M1 1 L11 9 L21 1" fill="none" stroke="#fff" stroke-width="1.6"/></svg>
</div>

<div class="abs sort-label">Sort by:</div>
<div class="abs select" style="left:315px;top:690px;width:111px">Latest<i>▲<br>▼</i></div>

<div class="abs listing-photo" role="img" aria-label="Two-storey brick family house with garage under a blue sky"></div>
<div class="abs listing-title">SURE TO BE A FAMILY FAVOURITE!</div>
<div class="abs meta-row">
  <div>AUD$ 650,000</div>
  <div class="deal">Buy</div>
  <div>House</div>
</div>
<div class="abs feat-row">
  <div><svg width="28" height="14" viewBox="0 0 28 14"><rect x="1" y="2" width="3" height="11" fill="#8a5a2a"/><rect x="4" y="6" width="23" height="4" fill="#8a5a2a"/><rect x="24" y="8" width="3" height="5" fill="#8a5a2a"/></svg>5</div>
  <div><svg width="28" height="18" viewBox="0 0 28 18"><path d="M2 8 H26 V11 Q26 16 20 16 H8 Q2 16 2 11 Z" fill="none" stroke="#8fb7c4" stroke-width="2"/><path d="M5 8 V3 Q5 1 8 1" fill="none" stroke="#8fb7c4" stroke-width="2"/></svg>2</div>
  <div><svg width="26" height="18" viewBox="0 0 26 18"><rect x="2" y="6" width="22" height="8" rx="2" fill="#7f8b2e"/><path d="M6 6 L8 1 H18 L20 6" fill="#7f8b2e"/><circle cx="7" cy="15" r="2.5" fill="#444"/><circle cx="19" cy="15" r="2.5" fill="#444"/></svg>2</div>
  <div class="loc"><svg width="10" height="14" viewBox="0 0 10 14"><path d="M5 14 C1 8 0 6 0 5 A5 5 0 0 1 10 5 C10 6 9 8 5 14 Z" fill="#444"/><circle cx="5" cy="5" r="2" fill="#f4f4f4"/></svg><span>Mornington,<br>Australia</span></div>
</div>
<div class="abs size">Building Size: <b>35 Sqm</b></div>
<div class="abs desc">Description</div>
<div class="abs agent-badge"></div>

<aside class="abs au-banner">
  <div class="au-count">120,000</div>
  <svg class="au-plus" width="60" height="60" viewBox="0 0 60 60"><rect x="22" y="0" width="16" height="60" fill="var(--green)"/><rect x="0" y="22" width="60" height="16" fill="var(--green)"/></svg>
  <div class="au-line" style="top:138px">NOW</div>
  <div class="au-line" style="top:172px">AVAILABLE</div>
  <div class="au-line" style="top:206px">IN</div>
  <div class="au-country">AUSTRALIA</div>
  <div class="au-art" role="img" aria-label="Map of Australia in flag colours above a hand holding a red house-shaped Just Listed sign"></div>
  <div class="au-cta">CLICK HERE</div>
</aside>

</body>
</html>
```